New website: Wandermeridia.com

We need to build a website for our small travel agency.
We want to be able to upload our brochures and offer our tours on site. No online payments involved yet.

We want to create an exact copy of another website: www.trailbrookvale.is, but with our own information and products. We like that design very much.

We are not going to do any sales via the website as the website above, but instead we want to show in the same style and everything the different tours that we offer.

We need to be able to modify tours: tour pictures, info, add videos, text, etc.

We need the website in English and Spanish. We can provide the Spanish translation.

We would advice you to create a copy of that website, with the text to be editable by us.
We own the website www.wandermeridia.com and need that the designer uploads it and makes it work as well.

We have uploaded some pictures that can be used as place markers.

I HAVE UPLOADED OUR BROCHURE DEMO SO YOU CAN GET MORE INFO IN ENGLISH ABOUT US AND MORE PICTURES.

PLEASE REMEMBER THAT THE WEBSITE ¨MOVES¨ when you resize it! Specially the pictures get ¨bigger¨ or smaller¨ when you resize. The same applies to the logos :-)

Once you have created the front page just as the original website I will select it and then we can put the real info and extra pages :-)

Tourists, international people traveling.

Tourism

Coded - Design and coding required

5+ page

Sans Serif

ffffff

• Exactly the same layout of the website mentioned (www.trailbrookvale.is)
• Everything the same, but with our own logo, texts and photos.
• HOME
• TOURS
• GROUPS
• OUR MOST POPULAR TOURS

```html
<!DOCTYPE html>
<html lang="en">
<head>
<meta charset="utf-8">
<title>Wandermeridia — Home</title>
<link href="https://fonts.googleapis.com/css2?family=Play:wght@400;700&family=Open+Sans:wght@400;600&display=swap" rel="stylesheet">
<style>
:root{
  --red:#e2282c;
  --ink:#222222;
  --muted:#555555;
  --panel:#f3f3f3;
  --line:#dddddd;
  --footer:#1d1d1d;
  --footer-text:#bbbbbb;
  --white:#ffffff;
}
*{box-sizing:border-box;margin:0;padding:0}
html,body{width:1200px;height:3557px;overflow:hidden;background:var(--white)}
body{position:relative;font-family:"Open Sans",Arial,sans-serif;color:var(--ink)}

/* header */
.site-header{position:absolute;left:0;top:0;width:1200px;height:111px}
.brand{position:absolute;left:100px;top:14px;width:86px;height:86px;border-radius:50%;background:#000;color:var(--white);display:flex;align-items:center;justify-content:center;font-family:"Play",sans-serif;font-size:12px;font-weight:700}
.main-nav{position:absolute;left:0;top:0;height:111px}
.main-nav a{position:absolute;top:50px;font-family:"Play",sans-serif;font-size:13px;color:var(--ink);text-decoration:none;letter-spacing:.5px;white-space:nowrap}
.main-nav a.active{color:var(--red)}
.nav-pin{position:absolute;left:480px;top:24px}
.search-icon{position:absolute;left:1018px;top:46px}
.lang{position:absolute;left:1051px;top:43px;width:52px;height:28px;border:1px solid #999;font-size:11px;display:flex;align-items:center;justify-content:center;gap:6px;font-family:"Play",sans-serif}

/* hero */
.hero-tile{position:absolute;overflow:hidden}
.hero-main{left:0;top:111px;width:598px;height:572px;background:linear-gradient(180deg,#5f7fa3 0%,#b7c5d3 35%,#6b6f6c 65%,#3b3a35 100%)}
.hero-top{left:605px;top:111px;width:595px;height:283px;background:linear-gradient(180deg,#8aa1ba 0%,#d2dbe3 40%,#4d5657 75%,#5d5a3e 100%)}
.hero-bottom{left:605px;top:401px;width:595px;height:282px;background:linear-gradient(180deg,#3f78b6 0%,#a6c2dc 45%,#5f7e8c 70%,#2d6d83 100%)}
.hero-caption{position:absolute;color:var(--white)}
.hero-caption h2{font-family:"Play",sans-serif;font-weight:400;font-size:33px;letter-spacing:1px}
.hero-caption p{font-family:"Play",sans-serif;font-size:15px;margin-top:4px;letter-spacing:.5px}
.hero-main .hero-caption{left:0;top:397px;width:403px;height:113px;background:rgba(160,40,40,.62);padding:22px 0 0 70px}
.hero-top .hero-caption{left:40px;top:130px}
.hero-bottom .hero-caption{left:40px;top:105px}
.slider-dots{position:absolute;left:580px;top:705px;display:flex;gap:6px}
.slider-dots span{width:5px;height:5px;border-radius:50%;background:#cccccc}
.slider-dots span.on{background:var(--red)}

/* tours */
.section-title{position:absolute;left:0;width:1200px;text-align:center;font-family:"Play",sans-serif;font-size:26px;font-weight:400;top:764px}
.tour-tabs{position:absolute;top:805px;left:0;width:1200px;display:flex;justify-content:center;font-size:11.5px;font-family:"Play",sans-serif;color:var(--ink)}
.tour-tabs span{padding:0 7px;border-left:1px solid #888;line-height:12px}
.tour-tabs span:first-child{border-left:none;color:var(--red);position:relative}
.tour-tabs span:first-child::after{content:"";position:absolute;left:-4px;right:0;bottom:-9px;height:2px;background:var(--red)}
.tour-card{position:absolute;width:313px}
.tour-photo{width:313px;height:261px}
.tour-card h3{font-family:"Play",sans-serif;font-weight:400;font-size:20px;line-height:23px;margin-top:27px;letter-spacing:.3px}
.tour-meta{font-size:11px;margin-top:5px;color:var(--ink)}
.tour-price{font-family:"Play",sans-serif;font-size:16px;color:var(--red);margin-top:2px}
.tour-price small{font-size:10px;color:var(--ink);margin-left:4px}

/* about blocks */
.about{position:absolute;left:0;width:1200px;background:var(--panel)}
.about-photo{position:absolute;top:0;width:420px;height:100%}
.about-copy{position:absolute;width:640px}
.about-copy h2{font-family:"Play",sans-serif;font-weight:400;font-size:25px;letter-spacing:2px;text-transform:uppercase}
.about-copy p{font-size:13.5px;line-height:24px;margin-top:28px;color:#333}

/* partners */
.partners{position:absolute;left:0;top:2929px;width:1200px;height:231px}

/* footer */
.site-footer{position:absolute;left:0;top:3160px;width:1200px;height:397px;background:var(--footer);color:var(--footer-text)}
.footer-brand{position:absolute;left:107px;top:68px;width:218px;height:218px;border-radius:50%;background:#000;color:var(--white);display:flex;align-items:center;justify-content:center;font-family:"Play",sans-serif;font-size:28px;font-weight:700}
.footer-col{position:absolute;top:72px}
.footer-col h4{font-family:"Play",sans-serif;font-weight:700;font-size:13px;color:var(--white);letter-spacing:1px;margin-bottom:24px}
.footer-col ul{list-style:none}
.footer-col li{font-family:"Play",sans-serif;font-size:11px;color:var(--white);height:31px;display:flex;align-items:center;gap:20px}
.footer-col li::before{content:"";width:22px;height:2px;background:var(--red);display:inline-block}
.contact-row{display:flex;gap:16px;font-size:11.5px;margin-bottom:24px;line-height:18px}
.contact-row svg{flex:none;margin-top:2px}
.social{display:flex;gap:14px;margin-top:6px}
.social span{width:14px;height:14px;border-radius:50%;background:#9a9a9a}
.copyright{position:absolute;left:0;top:3510px;width:1200px;text-align:center;font-size:11px;color:var(--footer-text)}
.copyright b{color:var(--white);font-weight:600}
</style>
</head>
<body>

<header class="site-header">
  <div class="brand">Wandermeridia</div>
  <nav class="main-nav">
    <svg class="nav-pin" width="16" height="20" viewBox="0 0 16 20"><path d="M8 0C3.6 0 0 3.4 0 7.6 0 13 8 20 8 20s8-7 8-12.4C16 3.4 12.4 0 8 0z" fill="#e2282c"/><circle cx="8" cy="7.5" r="2.8" fill="#000"/></svg>
    <a class="active" style="left:470px">HOME</a>
    <a style="left:548px">TOURS</a>
    <a style="left:629px">GROUPS</a>
    <a style="left:721px">RENT A CAR</a>
    <a style="left:837px">FLIGHT</a>
    <a style="left:918px">CONTACT</a>
  </nav>
  <svg class="search-icon" width="18" height="18" viewBox="0 0 18 18"><circle cx="7.5" cy="7.5" r="5.5" fill="none" stroke="#e2282c" stroke-width="2.2"/><line x1="11.5" y1="11.5" x2="16.5" y2="16.5" stroke="#e2282c" stroke-width="2.4"/></svg>
  <div class="lang">EN <svg width="7" height="5" viewBox="0 0 7 5"><path d="M0 0h7L3.5 5z" fill="#555"/></svg></div>
</header>

<section class="hero">
  <div class="hero-tile hero-main" role="img" aria-label="Travellers before granite mountain peaks and a lake">
    <div class="hero-caption"><h2>Lorem ipsum dolor</h2><p>consectetur adipiscing elit.</p></div>
  </div>
  <div class="hero-tile hero-top" role="img" aria-label="Mountain range above a lake under cloudy sky">
    <div class="hero-caption"><h2>Dolor Sit Amit Lorem</h2><p>consectetur adipiscing elit.</p></div>
  </div>
  <div class="hero-tile hero-bottom" role="img" aria-label="Blue lake with snowy peaks in the distance">
    <div class="hero-caption"><h2>Ipsum dolor</h2><p>consectetur adipiscing elit.</p></div>
  </div>
  <div class="slider-dots"><span class="on"></span><span></span><span></span><span></span></div>
</section>

<section class="popular-tours">
  <h2 class="section-title">Our most popular tours</h2>
  <div class="tour-tabs"><span>Popular Tours</span><span>Day Tours</span><span>Travel by Air Tours</span><span>Self Drive Tours</span><span>Adventures Tours</span><span>Customize Tours</span><span>Transfer</span></div>

  <article class="tour-card" style="left:100px;top:866px">
    <div class="tour-photo" role="img" aria-label="Lake with lodge and mountains" style="background:linear-gradient(180deg,#3f73b0,#b9cde0 45%,#5f8ea3 70%,#2e7795)"></div>
    <h3>Volcanoes &amp; Glaciers from up above</h3><p class="tour-meta">length: 2 – 2,5 hours, including 1 landing</p><p class="tour-price">135.900<small>ISK</small></p>
  </article>
  <article class="tour-card" style="left:444px;top:866px">
    <div class="tour-photo" role="img" aria-label="Road leading toward dark mountains" style="background:linear-gradient(180deg,#5a86bb,#d6dfe8 40%,#4a4c46 70%,#6d6a5a)"></div>
    <h3>Volcanoes &amp; Glaciers from up above</h3><p class="tour-meta">length: 2 – 2,5 hours, including 1 landing</p><p class="tour-price">135.900<small>ISK</small></p>
  </article>
  <article class="tour-card" style="left:788px;top:866px">
    <div class="tour-photo" role="img" aria-label="Marble caves over turquoise water" style="background:linear-gradient(180deg,#8a8f94,#b9c3c8 45%,#4fb0be 75%,#1f8a9c)"></div>
    <h3>Volcanoes &amp; Glaciers from up above</h3><p class="tour-meta">length: 2 – 2,5 hours, including 1 landing</p><p class="tour-price">135.900<small>ISK</small></p>
  </article>
  <article class="tour-card" style="left:100px;top:1276px">
    <div class="tour-photo" role="img" aria-label="Driftwood in a mirror lake below peaks" style="background:linear-gradient(180deg,#1f4f8f,#7fa5c9 40%,#2f5d87 70%,#1d3f66)"></div>
    <h3>Volcanoes &amp; Glaciers from up above</h3><p class="tour-meta">length: 2 – 2,5 hours, including 1 landing</p><p class="tour-price">135.900<small>ISK</small></p>
  </article>
  <article class="tour-card" style="left:444px;top:1276px">
    <div class="tour-photo" role="img" aria-label="Road through autumn hills toward granite towers" style="background:linear-gradient(180deg,#6f98c9,#c8cfd2 40%,#9a8a5a 70%,#b08a3a)"></div>
    <h3>Volcanoes &amp; Glaciers from up above</h3><p class="tour-meta">length: 2 – 2,5 hours, including 1 landing</p><p class="tour-price">135.900<small>ISK</small></p>
  </article>
  <article class="tour-card" style="left:788px;top:1276px">
    <div class="tour-photo" role="img" aria-label="Waterfall among autumn vegetation" style="background:linear-gradient(180deg,#7a7f86,#9a8f7a 40%,#8f5a2a 70%,#3f5a3a)"></div>
    <h3>Volcanoes &amp; Glaciers from up above</h3><p class="tour-meta">length: 2 – 2,5 hours, including 1 landing</p><p class="tour-price">135.900<small>ISK</small></p>
  </article>
</section>

<section class="about" style="top:1724px;height:404px">
  <div class="about-photo" style="left:0;background:linear-gradient(160deg,#9fc8ea,#e9eef4 45%,#f2c8d4 80%,#d99aae)" role="img" aria-label="Pale pink blossoms against a blue sky"></div>
  <div class="about-copy" style="left:444px;top:106px">
    <h2>Quienes somos</h2>
    <p>Somos una empresa conformada por un idóneo equipo de trabajo que consta de alta motivación, óptimo entrenamiento, elevado capital humano y cuyos integrantes poseen más de 10 años de experiencia trabajando en forma independiente en Turismo Receptivo Regional, Nacional e Internacional. En conjunto nos potenciamos y logramos satisfacer las altas demandas de servicios turísticos requeridos por nuestros clientes.</p>
  </div>
</section>

<section class="about" style="top:2128px;height:401px">
  <div class="about-copy" style="left:97px;top:101px">
    <h2>Mision</h2>
    <p>Nuestra misión es ofrecer servicios de Turismo Receptivo para la Región de Magallanes y Antártica Chilena que cumplan con las exigencias de calidad y valor humano que nuestros clientes solicitan. Para lograrlo, trabajamos en conjunto con proveedores turísticos seleccionados y nos enfocamos hacia la excelencia de un servicio personalizado, sirviendo con pasión, experiencia y responsabilidad a cada uno de nuestros clientes.</p>
  </div>
  <div class="about-photo" style="left:780px;background:linear-gradient(180deg,#c9c9c9,#8a8a8a 55%,#3a3a3a)" role="img" aria-label="Black and white lakeshore with a small boat"></div>
</section>

<section class="about" style="top:2529px;height:400px">
  <div class="about-photo" style="left:0;background:linear-gradient(160deg,#2b2f6b,#6a3f7f 40%,#e58a7a 70%,#f6c27a)" role="img" aria-label="Sunset glowing through silhouetted hands"></div>
  <div class="about-copy" style="left:444px;top:100px">
    <h2>Vision</h2>
    <p>Nuestra visión es crear una Plataforma de Servicios Logísticos y Turísticos para la Ecorregión Sub-Antártica y Antártica que una toda la oferta turística de la zona a través de una red local, nacional y global de proveedores, con el objetivo de mejorar, a través de la cuidadosa selección de prestadores, la accesibilidad por parte del cliente, la competitividad dentro del mercado, facilitando la inclusión de pequeñas y medianas empresas.</p>
  </div>
</section>

<section class="partners" aria-label="Partner badges">
  <svg width="1200" height="231" viewBox="0 0 1200 231">
    <g fill="#3a3a3a">
      <circle cx="178" cy="114" r="36"/>
      <rect x="309" y="84" width="60" height="60"/>
      <circle cx="510" cy="114" r="36"/>
      <rect x="646" y="84" width="60" height="60"/>
      <circle cx="842" cy="114" r="36"/>
      <rect x="983" y="84" width="60" height="60"/>
    </g>
  </svg>
</section>

<footer class="site-footer">
  <div class="footer-brand">Wandermeridia</div>
  <div class="footer-col" style="left:420px">
    <h4>MENU</h4>
    <ul><li>HOME</li><li>TOURS</li><li>GROUPS</li><li>RENT A CAR</li><li>FLIGHT</li><li>CONTACT</li></ul>
  </div>
  <div class="footer-col" style="left:633px">
    <h4>MENU</h4>
    <ul><li>HOW TO BOOK</li><li>BOOKING TERMS</li><li>PRIVACY POLICY</li><li>FAQ</li><li>Terms &amp; Conditions</li></ul>
  </div>
  <div class="footer-col" style="left:866px;width:240px">
    <h4>CONTACT</h4>
    <div class="contact-row"><svg width="14" height="11" viewBox="0 0 14 11"><rect x=".5" y=".5" width="13" height="10" fill="none" stroke="#bbb"/><path d="M.5 .5 7 6l6.5-5.5" fill="none" stroke="#bbb"/></svg><span>info@wandermeridia.com</span></div>
    <div class="contact-row"><svg width="13" height="13" viewBox="0 0 13 13"><path d="M3 0 5 3 3.5 5C4.5 7 6 8.5 8 9.5L10 8l3 2-1.5 3C6 12.5.5 7 0 1.5z" fill="#bbb"/></svg><span>(555) 014-2093</span></div>
    <div class="contact-row"><svg width="11" height="14" viewBox="0 0 11 14"><path d="M5.5 0C2.5 0 0 2.3 0 5.2 0 9 5.5 14 5.5 14S11 9 11 5.2C11 2.3 8.5 0 5.5 0z" fill="#bbb"/><circle cx="5.5" cy="5.2" r="2" fill="#1d1d1d"/></svg><span>1280 Harbor Lane<br>Puerto Sur , 40317</span></div>
    <div class="social" aria-label="Social links"><span></span><span></span><span></span><span></span><span></span><span></span></div>
  </div>
</footer>
<p class="copyright"><b>Copyrights 2016</b> © Wandermeridia, All Rights Reserved</p>

</body>
</html>
```